3 JPG Website Page Mockups need tidying / made into layered PSDs

Our website is aimed at creating a financial eduction site for females.

We have mockups of each page which are provided in jpeg.... but they need to be tidied up, layered into PSD (with descriptive layer names to allow coding from and no flattening - each object needs it's own layer) and we welcome any creative improvements suggested (although we are pretty happy with the way it's laid out at the moment as it is), without changing the feel, colour scheme or functionality of the site.

Three pages are needed:
Home page when not logged in
Home page when logged in
Topic header page

Please just upload the homepage to bid for the job... the winning designer will then have 5 days after they've been chosen to supply the psds of the other 2 pages .

I have also uploaded an image that can be used as a placeholder in the top box.
Thanks
Updates

As requested... Current font is Gill Sans MT

Thanks

Hi
Thanks for your designs.... For those of you still using the 4 circles (which I quite like), but haven't yet done so, could you see if you can move them around slightly to that the words don't get covered by the next circle?

Thanks

Reason: Designe has asked for An extension to work on new icons... would like to give them the time to see what they come up with, thanks

Industry/Entity Type

Financial

Requirements
Must have
• Maintain current feel & colour scheme of the website

```html
<!DOCTYPE html>
<html lang="en">
<head>
<meta charset="utf-8">
<title>The Money Compass – Home</title>
<link href="https://fonts.googleapis.com/css2?family=Arimo:wght@400;700&family=Roboto+Condensed:wght@400;700&display=swap" rel="stylesheet">
<style>
:root{
  --teal:#138f94;
  --teal-dark:#0b7479;
  --teal-text:#3f7e8c;
  --head-grey:#efefef;
  --frame-green:#7fb07f;
  --green-text:#5d9a5d;
  --sage:#a3c49a;
  --pale-blue:#dfeaf4;
  --beige:#f4ecc8;
  --orange:#f7781f;
  --orange-light:#fb9a47;
  --ink:#222;
}
*{box-sizing:border-box;margin:0;padding:0}
html,body{width:1200px;height:942px;overflow:hidden;background:#fff}
body{position:relative;font-family:"Arimo",Arial,sans-serif;color:var(--ink)}
.abs{position:absolute}

/* top navigation */
.topnav{left:0;top:0;width:1200px;height:29px;background:linear-gradient(#1aa1a6,var(--teal-dark))}
.home-tab{left:165px;top:5px;width:45px;height:24px;background:var(--head-grey);border-radius:3px 3px 0 0}
.topnav a{position:absolute;top:7px;color:#fff;font-size:15px;text-decoration:none;transform:translateX(-50%);white-space:nowrap}
.locale{left:986px;top:8px;color:#fff;font-size:10px;display:flex;align-items:center;gap:4px}
.flag{width:19px;height:13px;background:#1d3d8c;position:relative}
.flag::before{content:"";position:absolute;left:0;top:0;width:9px;height:6px;background:linear-gradient(#fff 0 0) center/9px 2px no-repeat,linear-gradient(#fff 0 0) center/2px 6px no-repeat,#1d3d8c}

/* header band */
.header{left:0;top:29px;width:1200px;height:117px;background:var(--head-grey)}
.logo{left:165px;top:56px;font-size:58px;color:#4a4a4a;letter-spacing:-1px;line-height:1}
.search-label{left:362px;top:48px;font-size:13px;font-weight:700;color:var(--teal)}
.search{left:347px;top:68px;width:377px;height:33px;background:#fff;border:1px solid #ccc;border-radius:17px;box-shadow:inset 0 1px 2px rgba(0,0,0,.12)}
.search .placeholder{position:absolute;left:15px;top:8px;font-size:15px;color:#8a8a8a;white-space:nowrap}
.search .go{position:absolute;right:8px;top:6px;width:19px;height:19px;border-radius:50%;background:#2d8be0}
.pill{top:68px;height:33px;border:1px solid #ccc;border-radius:17px;background:linear-gradient(#fff,#ececec);font-size:12px;color:#222;display:flex;align-items:center;gap:7px;padding-left:8px}
.dot-arrow{width:18px;height:18px;border-radius:50%;background:#3a8fe0;display:flex;align-items:center;justify-content:center}
.sublink{top:115px;font-size:11px;font-weight:700;color:var(--teal-text);text-align:center}
.sublink svg{display:block;margin:2px auto 0}

/* welcome row */
.welcome{left:165px;top:164px;font-size:21px;color:var(--teal-text)}
.member{top:171px;font-size:12px;display:flex;align-items:center;gap:6px}
.orange-dot{width:16px;height:16px;border-radius:50%;background:var(--orange-light);color:#fff;font-size:12px;font-weight:700;display:flex;align-items:center;justify-content:center;line-height:1}

/* hero */
.hero{left:166px;top:207px;width:867px;height:230px;border:1px solid var(--frame-green);border-radius:4px;overflow:hidden}
.hero-photo{position:absolute;right:0;top:0;width:400px;height:100%;background:linear-gradient(90deg,#fff 0%,#efe3d8 25%,#c98a5a 55%,#8a4b2a 80%,#b87a50 100%)}
.hero h1{position:absolute;left:33px;top:22px;font-weight:400;font-size:29px;line-height:33px;color:var(--teal-text)}
.join{position:absolute;left:31px;top:147px;width:364px;height:60px;border-radius:30px;background:linear-gradient(var(--orange-light),var(--orange));color:#fff;font-size:24px;font-weight:700}
.join .c{position:absolute;left:24px;top:15px;width:40px;height:32px;border-radius:50%;background:#fff;display:flex;align-items:center;justify-content:center}
.join b{position:absolute;left:110px;top:15px}
.caption{position:absolute;left:751px;top:151px;width:110px;height:39px;background:rgba(255,255,255,.85);border-radius:3px;font-size:10px;padding:6px 10px;line-height:13px;color:#333}
.pager{position:absolute;left:702px;top:196px;width:159px;height:28px;background:rgba(255,255,255,.9);border-radius:3px;font-size:10px;color:var(--green-text);display:flex;align-items:center;justify-content:space-around;padding:0 6px}
.pager .on{color:#222;text-decoration:underline;font-weight:700}

/* topic box */
.topic{left:166px;top:452px;width:867px;height:231px;border:1px solid var(--frame-green);border-radius:4px}
.video{left:198px;top:456px;width:270px;height:222px;border:1px solid #ddd;border-radius:4px;background:#fff}
.video-img{position:absolute;left:7px;top:7px;width:255px;height:192px;background:linear-gradient(135deg,#3a2a22,#5b3a2c 50%,#2a2420)}
.play{position:absolute;left:113px;top:73px;width:50px;height:49px;background:rgba(30,30,30,.8);display:flex;align-items:center;justify-content:center}
.lower-third{position:absolute;left:24px;top:139px;width:141px;height:44px;background:rgba(110,150,110,.9);color:#eee;padding:4px 6px;font-size:12px;line-height:11px;letter-spacing:1px;font-variant:small-caps}
.lower-third small{font-size:8px;display:block;letter-spacing:.5px}
.controls{position:absolute;left:7px;top:200px;width:255px;height:14px;background:linear-gradient(#eee,#d8d8d8);font-size:8px;color:var(--green-text);display:flex;align-items:center;gap:6px;padding:0 4px}
.controls .track{flex:1;height:3px;background:#bbb}
.kicker{left:499px;top:467px;font-size:11px;font-weight:700;color:var(--teal-text)}
.topic h2{position:absolute;left:332px;top:35px;font-weight:400;font-size:29px;line-height:34px;color:var(--teal-text)}
.learn{left:502px;top:565px;font-size:12px;font-weight:700;color:var(--green-text)}

.bubble{border-radius:50%;font-family:"Roboto Condensed",Arial,sans-serif;text-align:center}
.b-guide{left:650px;top:590px;width:80px;height:80px;background:#fff;border:4px solid var(--sage);color:#333;font-size:11px;padding-top:16px;line-height:1}
.b-guide big{font-size:20px;display:block}
.b-guide em{font-style:normal;color:var(--green-text);font-size:12px}
.b-poll{left:718px;top:552px;width:112px;height:112px;background:var(--pale-blue);border:1px solid var(--sage);font-size:15px;color:#333}
.b-real{left:812px;top:510px;width:100px;height:100px;background:#fff;border:6px solid var(--beige);font-size:14px;color:#333;text-align:left;padding:14px 0 0 12px;line-height:16px}
.b-ask{left:893px;top:548px;width:136px;height:136px;background:var(--sage);border:3px solid #fff;box-shadow:0 0 0 1px var(--sage);color:#fff;font-family:"Arimo",Arial,sans-serif;font-size:11px;font-weight:700;line-height:14px;padding:20px 12px 0}

/* icon row */
.tile{left:182px;top:710px;width:109px;height:80px;background:linear-gradient(#e06b2c,#f08a52 65%,#fff);font-size:12px;font-weight:700;text-align:center;color:#222}
.tile svg{display:block;margin:4px auto 2px}
.icon{top:720px;width:60px;height:60px}
</style>
</head>
<body>

<nav class="abs topnav">
  <div class="abs home-tab"><svg width="45" height="24" viewBox="0 0 45 24"><path d="M22.5 7l-5 4.5h1.5V16h7v-4.5H27.5z" fill="var(--teal)"/></svg></div>
  <a style="left:268px">Polls</a>
  <a style="left:347px">Events</a>
  <a style="left:462px">Learning Centre</a>
  <a style="left:612px">Find and Adviser</a>
  <a style="left:759px">Ask a Question</a>
  <a style="left:880px">About Us</a>
  <div class="abs locale"><span class="flag"></span>AU ▾</div>
</nav>

<header class="abs header"></header>
<div class="abs logo">LOGO</div>
<div class="abs search-label">What are you looking for?</div>
<div class="abs search"><span class="placeholder">Search The Money Compass for...</span>
  <span class="go"><svg width="19" height="19" viewBox="0 0 19 19"><circle cx="8.5" cy="8.5" r="3.5" fill="none" stroke="#fff" stroke-width="1.6"/><path d="M11 11l3 3" stroke="#fff" stroke-width="1.8"/></svg></span></div>
<div class="abs pill" style="left:787px;width:122px"><span class="dot-arrow"><svg width="8" height="8"><path d="M2 1l3 3-3 3" stroke="#fff" stroke-width="1.6" fill="none"/></svg></span>Find an Adviser</div>
<div class="abs pill" style="left:913px;width:122px"><span class="dot-arrow"><svg width="8" height="8"><path d="M2 1l3 3-3 3" stroke="#fff" stroke-width="1.6" fill="none"/></svg></span>Contact Us</div>
<div class="abs sublink" style="left:356px">Popular Searches<svg width="14" height="8"><path d="M2 1l5 5 5-5" stroke="var(--teal)" stroke-width="2.4" fill="none"/></svg></div>
<div class="abs sublink" style="left:472px">Explore the Learning Centre<svg width="14" height="8"><path d="M2 1l5 5 5-5" stroke="var(--teal)" stroke-width="2.4" fill="none"/></svg></div>
<div class="abs sublink" style="left:638px">Ask a Question<svg width="14" height="8"><path d="M2 1l5 5 5-5" stroke="var(--teal)" stroke-width="2.4" fill="none"/></svg></div>

<div class="abs welcome">Welcome to the New Money Compass Site</div>
<div class="abs member" style="left:697px">Already a member?</div>
<div class="abs member" style="left:820px"><span class="orange-dot">+</span><b>Login</b></div>
<div class="abs member" style="left:895px"><span class="orange-dot">›</span><b>Forgotten password</b></div>

<section class="abs hero">
  <div class="hero-photo" role="img" aria-label="Photo of a smiling member standing by a staircase"></div>
  <h1>We're building Australia's<br>biggest community dedicated to the<br>Financial Empowerment of Women</h1>
  <div class="join"><span class="c"><svg width="14" height="16"><path d="M4 2l6 6-6 6" stroke="var(--orange)" stroke-width="3" fill="none"/></svg></span><b>Join Now for Free</b></div>
  <div class="caption"><b>Elena</b><br>Member since 2006</div>
  <div class="pager"><span>Previous</span><span>1</span><span>2</span><span>3</span><span class="on">4</span><span>Next</span></div>
</section>

<section class="abs topic">
  <h2>Tomorrow Can Belong to Those<br>Who Prepare Today</h2>
</section>
<div class="abs video">
  <div class="video-img" role="img" aria-label="Video still of a speaker in front of bookshelves">
    <div class="play"><svg width="18" height="20"><path d="M2 1l15 9-15 9z" fill="#fff"/></svg></div>
    <div class="lower-third">Dana Whitford<small>Founder, Chairman &amp; CEO<br>Harbor &amp; Co.</small></div>
  </div>
  <div class="controls"><span>▶ ■</span><span>00:00</span><span class="track"></span><span>00:00</span><span>⛶ ◂||||</span></div>
</div>
<div class="abs kicker">JULY TOPIC: PREPARING FOR RETIREMENT</div>
<div class="abs learn">Learn More ›</div>

<div class="abs bubble b-real">Real Women<br>Real Stories<br><span style="color:var(--green-text);font-size:12px">See Video ›</span></div>
<div class="abs bubble b-poll">
  <svg width="100" height="40" viewBox="0 0 100 40" style="margin:22px auto 0;display:block">
    <g fill="var(--sage)"><rect x="4" y="31" width="7" height="7"/><rect x="14" y="29" width="7" height="9"/><rect x="24" y="26" width="7" height="12"/><rect x="34" y="20" width="7" height="18"/><rect x="44" y="15" width="7" height="23"/><rect x="54" y="10" width="7" height="28"/><rect x="64" y="6" width="7" height="32"/><rect x="74" y="8" width="7" height="30"/><rect x="84" y="14" width="7" height="24"/></g></svg>
  Take Our Poll<br><span style="color:var(--green-text);font-size:12px">Vote ›</span></div>
<div class="abs bubble b-guide">5 Minute<big>Guide</big><em>PDF ›</em></div>
<div class="abs bubble b-ask">Have questions about Life Stages &amp; Planning? Ask a Question or see what others have asked...<br><span style="display:block;margin-top:4px">More ›</span></div>

<div class="abs tile"><svg width="50" height="48" viewBox="0 0 50 48"><circle cx="25" cy="15" r="11" fill="#fff"/><path d="M3 46c0-14 10-20 22-20s22 6 22 20z" fill="#fff"/></svg>Welcome</div>
<div class="abs icon" role="img" aria-label="Community icon" style="left:347px"><svg width="60" height="60"><rect x="0" y="9" width="46" height="46" rx="8" fill="#a3123f"/></svg></div>
<div class="abs icon" role="img" aria-label="Video library icon" style="left:439px"><svg width="60" height="60"><circle cx="30" cy="30" r="28" fill="#9a9a9a"/></svg></div>
<div class="abs icon" role="img" aria-label="Home and property icon" style="left:539px"><svg width="60" height="60"><path d="M2 28l28-24 28 24v30H2z" fill="#d9d9d9"/><path d="M2 28l28-24 28 24" fill="#d7262c"/></svg></div>
<div class="abs icon" role="img" aria-label="Investment chart icon" style="left:650px"><svg width="60" height="60"><rect x="1" y="6" width="58" height="50" rx="3" fill="#ececec" stroke="#bbb"/><path d="M6 44l10-12 8 8 10-16 8 10 12-14" stroke="#c2185b" fill="none" stroke-width="1.5"/></svg></div>
<div class="abs icon" role="img" aria-label="Stopwatch and notes icon" style="left:769px"><svg width="60" height="60"><rect x="22" y="6" width="34" height="48" fill="#f2f5e8" transform="rotate(12 39 30)"/><circle cx="20" cy="38" r="17" fill="#2878d0"/></svg></div>
<div class="abs icon" role="img" aria-label="Helping hands icon" style="left:853px"><svg width="60" height="60"><path d="M10 34l26-26 14 10-26 28z" fill="#1aa2b0"/></svg></div>
<div class="abs icon" role="img" aria-label="Wellbeing icon" style="left:947px"><svg width="64" height="64"><circle cx="32" cy="30" r="32" fill="#2e9b3b"/></svg></div>

</body>
</html>
```